Talvern Asset Management - Corporate Letter Head Project

Looking for a classy design based on our current logo. Please find current logo source file in files. With our color scheme.

Target Market(s)

We're an investment firm, the letterhead needs to look professional and attractive to clients.

Industry/Entity Type

Hedgefund

Colors
0054AA
0677BA
7BADD7
CADEEF
E8F1F8

Requirements
Must have
• Our logo, address, phone number, and email

```html
<!DOCTYPE html>
<html lang="en">
<head>
<meta charset="utf-8">
<title>Talvern Asset Management – Letterhead</title>
<link rel="stylesheet" href="https://fonts.googleapis.com/css2?family=Crimson+Text:wght@400;700&display=swap">
<style>
  :root {
    --backdrop: #d9dbde;
    --paper: #f1f1f1;
    --pattern-light: #ebecee;
    --pattern-dark: #e3e5e8;
    --navy: #0f2a48;
    --blue: #0677ba;
    --text: #1c2433;
  }
  * { margin: 0; padding: 0; box-sizing: border-box; }
  html, body {
    width: 1014px;
    height: 1200px;
    overflow: hidden;
    background: var(--backdrop);
  }
  .letterhead {
    position: absolute;
    left: 96px;
    top: 20px;
    width: 821px;
    height: 1160px;
    background: var(--paper);
    font-family: "Crimson Text", Georgia, serif;
    color: var(--text);
    overflow: hidden;
  }
  .network-backdrop {
    position: absolute;
    inset: 0 0 19px 0;
    background: radial-gradient(ellipse at 45% 50%, var(--pattern-dark) 0%, var(--pattern-light) 40%, var(--paper) 75%);
  }
  .brand {
    position: absolute;
    right: 28px;
    top: 79px;
    width: 260px;
    text-align: center;
    color: var(--navy);
  }
  .brand-square {
    display: block;
    width: 85px;
    height: 85px;
    margin: 0 auto 20px;
    border: 2px solid var(--navy);
  }
  .brand-name {
    font-size: 29px;
    line-height: 1;
    letter-spacing: 0.3px;
    font-weight: 400;
    white-space: nowrap;
  }
  .brand-sub {
    margin-top: 3px;
    font-size: 14px;
    line-height: 1.2;
    letter-spacing: 10.5px;
    padding-left: 10.5px;
    font-weight: 400;
    white-space: nowrap;
  }
  .footer-rule {
    position: absolute;
    left: 47px;
    right: 46px;
    top: 1020px;
    height: 0;
    border-top: 1.5px solid var(--navy);
  }
  .contact-list {
    position: absolute;
    left: 47px;
    top: 1041px;
    list-style: none;
    font-size: 14.5px;
    letter-spacing: 0.6px;
    line-height: 20px;
  }
  .contact-list li {
    display: flex;
    align-items: center;
    gap: 12px;
  }
  .contact-list svg { width: 12px; height: 12px; fill: var(--navy); }
  .address {
    position: absolute;
    right: 46px;
    top: 1041px;
    text-align: right;
    font-size: 14.5px;
    letter-spacing: 0.6px;
    line-height: 20px;
    font-style: normal;
  }
  .address strong { font-weight: 700; }
  .base-band {
    position: absolute;
    left: 0;
    bottom: 0;
    width: 100%;
    height: 19px;
  }
</style>
</head>
<body>
  <main class="letterhead">
    <div class="network-backdrop" role="img" aria-label="Faint grey network of connected nodes across the sheet"></div>

    <header class="brand">
      <span class="brand-square"></span>
      <div class="brand-name">TALVERN ASSET</div>
      <div class="brand-sub">MANAGEMENT</div>
    </header>

    <div class="footer-rule"></div>

    <ul class="contact-list">
      <li>
        <svg viewBox="0 0 24 24" aria-hidden="true"><path d="M6.6 10.8a15.1 15.1 0 0 0 6.6 6.6l2.2-2.2c.3-.3.7-.4 1-.2 1.1.4 2.3.6 3.6.6.6 0 1 .4 1 1V20c0 .6-.4 1-1 1A17 17 0 0 1 3 4c0-.6.4-1 1-1h3.5c.6 0 1 .4 1 1 0 1.3.2 2.5.6 3.6.1.3 0 .7-.2 1z"/></svg>
        <span>312.555.0148</span>
      </li>
      <li>
        <svg viewBox="0 0 24 24" aria-hidden="true"><path d="M2 5h20v14H2z M3 6l9 7 9-7" /></svg>
        <span>contact@talvernam.com</span>
      </li>
      <li>
        <svg viewBox="0 0 24 24" aria-hidden="true"><circle cx="12" cy="12" r="10"/></svg>
        <span>www.talvernam.com</span>
      </li>
    </ul>

    <address class="address">
      <strong>Talvern Asset Management</strong><br>
      48 Harbor Lane, Suite 100<br>
      Boston, MA 02110, USA
    </address>

    <svg class="base-band" viewBox="0 0 821 19" preserveAspectRatio="none" aria-hidden="true">
      <polygon points="0,0 600,0 588,19 0,19" fill="var(--navy)"/>
      <polygon points="611,0 821,0 821,19 599,19" fill="var(--blue)"/>
    </svg>
  </main>
</body>
</html>
```